BRD business cards Dr. Martin Velk

I need a business card designed for our dental office. We are a "general dental" practice.
Looking for a clean, professional but not too fancy design with our logo and contact information required.
front of card is information/standard business card, backside is appt reminder with lines for date and time of appt
doctors name: Dr. Martin Velk DMD
office name: Velk Family Dental
address: 4827 E Tolland Ave Marlow Heights, OR 97412
phone: 503-555-0173
Dentistry
Office name, Doctor name, address, phone number...etc
- White/off white base color, blue and or black lettering

```html
<!DOCTYPE html>
<html lang="en">
<head>
<meta charset="utf-8">
<title>Velk Family Dental – Business Card</title>
<link href="https://fonts.googleapis.com/css2?family=EB+Garamond:wght@400;500;600&display=swap" rel="stylesheet">
<style>
  :root {
    --ink: #111111;
    --paper: #ffffff;
    --backdrop: #d9d9d9;
    --rule: #1a1a1a;
    --muted: #333333;
  }
  * { box-sizing: border-box; margin: 0; padding: 0; }
  html, body { width: 1200px; height: 900px; overflow: hidden; }
  body {
    background: var(--backdrop);
    font-family: "EB Garamond", Georgia, serif;
    color: var(--ink);
    display: flex;
    align-items: center;
    justify-content: center;
    gap: 40px;
  }
  .card {
    width: 520px;
    height: 297px;
    background: var(--paper);
    border-radius: 14px;
    position: relative;
    overflow: hidden;
    box-shadow: 0 6px 18px rgba(0,0,0,0.25);
  }

  /* Front */
  .brand {
    position: absolute;
    left: 40px;
    top: 40px;
    display: flex;
    align-items: center;
    gap: 12px;
  }
  .brand-dot {
    width: 34px; height: 34px;
    border: 2px solid var(--ink);
    border-radius: 50%;
    flex: none;
  }
  .brand-name {
    font-size: 26px;
    font-weight: 600;
    letter-spacing: 1.5px;
    text-transform: uppercase;
    color: var(--ink);
    white-space: nowrap;
  }
  .brand-rule {
    position: absolute;
    left: 40px; top: 92px;
    width: 250px; height: 2px;
    background: var(--rule);
  }
  .front-divider {
    position: absolute;
    left: 0; right: 0; top: 128px;
    height: 1.5px;
    background: var(--rule);
  }
  .contact {
    position: absolute;
    left: 22px; top: 142px;
    font-size: 14px;
    line-height: 1.45;
    list-style: none;
  }
  .contact li { display: flex; align-items: center; gap: 6px; white-space: nowrap; }
  .contact svg { width: 11px; height: 11px; fill: var(--ink); flex: none; }
  .doctor {
    position: absolute;
    right: 30px; top: 218px;
    font-size: 21px;
    font-weight: 600;
    letter-spacing: 1px;
    text-transform: uppercase;
    white-space: nowrap;
  }
  .doctor-rule {
    position: absolute;
    right: 30px; top: 252px;
    width: 340px; height: 1.5px;
    background: var(--rule);
  }

  /* Back */
  .back-band {
    height: 78px;
    background: var(--ink);
    display: flex;
    align-items: center;
    justify-content: center;
    gap: 14px;
  }
  .back-band .brand-name { color: var(--paper); font-size: 24px; }
  .back-band .brand-dot { border-color: var(--paper); width: 26px; height: 26px; }
  .appt {
    padding: 14px 28px 0;
    font-size: 14px;
  }
  .appt-title {
    text-align: center;
    font-size: 18px;
    font-weight: 600;
    letter-spacing: 1px;
    text-transform: uppercase;
    margin-bottom: 12px;
  }
  .field-row {
    display: flex;
    align-items: flex-end;
    gap: 6px;
    margin-bottom: 11px;
    white-space: nowrap;
  }
  .fill {
    flex: 1;
    border-bottom: 1.5px dashed var(--muted);
    height: 12px;
  }
  .fill.short { flex: 0.7; }
  .days {
    display: flex;
    justify-content: space-between;
    list-style: none;
    margin-top: 16px;
    padding: 0 8px;
  }
  .days li { display: flex; align-items: center; gap: 6px; font-size: 15px; }
  .box { width: 13px; height: 13px; border: 1.5px solid var(--ink); }
</style>
</head>
<body>

  <section class="card card-front" aria-label="Business card front">
    <div class="brand">
      <span class="brand-dot"></span>
      <span class="brand-name">Velk Family Dental</span>
    </div>
    <div class="brand-rule"></div>
    <div class="front-divider"></div>
    <ul class="contact">
      <li>
        <svg viewBox="0 0 24 24" aria-hidden="true"><path d="M6.6 10.8a15.1 15.1 0 0 0 6.6 6.6l2.2-2.2a1 1 0 0 1 1-.25 11.4 11.4 0 0 0 3.6.57 1 1 0 0 1 1 1V20a1 1 0 0 1-1 1A17 17 0 0 1 3 4a1 1 0 0 1 1-1h3.5a1 1 0 0 1 1 1c0 1.25.2 2.45.57 3.57a1 1 0 0 1-.25 1z"/></svg>
        503-555-0173
      </li>
      <li>
        <svg viewBox="0 0 24 24" aria-hidden="true"><path d="M12 2a7 7 0 0 0-7 7c0 5.25 7 13 7 13s7-7.750 7-13a7 7 0 0 0-7-7zm0 9.5A2.5 2.5 0 1 1 12 6.5a2.5 2.5 0 0 1 0 5z"/></svg>
        4827 E Tolland Ave Marlow Heights, OR 97412
      </li>
    </ul>
    <p class="doctor">Dr. Martin Velk DMD</p>
    <div class="doctor-rule"></div>
  </section>

  <section class="card card-back" aria-label="Appointment reminder card back">
    <header class="back-band">
      <span class="brand-dot"></span>
      <span class="brand-name">Velk Family Dental</span>
    </header>
    <div class="appt">
      <h2 class="appt-title">Your Next Appointment</h2>
      <div class="field-row"><span>Patient name:</span><span class="fill"></span></div>
      <div class="field-row">
        <span>Day:</span><span class="fill short"></span>
        <span>Date:</span><span class="fill short"></span>
        <span>Time</span><span class="fill short"></span><span>AM/PM</span>
      </div>
      <div class="field-row">
        <span>Day:</span><span class="fill short"></span>
        <span>Date:</span><span class="fill short"></span>
        <span>Time</span><span class="fill short"></span><span>AM/PM</span>
      </div>
      <ul class="days">
        <li><span class="box"></span>Mon</li>
        <li><span class="box"></span>Tue</li>
        <li><span class="box"></span>Wed</li>
        <li><span class="box"></span>Thu</li>
        <li><span class="box"></span>Fri</li>
      </ul>
    </div>
  </section>

</body>
</html>
```